Professional Services (B-2-B) Business Cards (Front & Back)

Corvantis is a business-to-business professional services company in the legal sector. They typically present to c-suite and executive functions who are looking for providers with expertise, and experience. Our business card should look and feel professional and contemporary, but we are not a startup tech company, so we want the tone to be more mature.

```html
<!DOCTYPE html>
<html lang="en">
<head>
<meta charset="utf-8">
<title>Corvantis Business Cards</title>
<link rel="stylesheet" href="https://fonts.googleapis.com/css2?family=Arimo:wght@400;700&display=swap">
<style>
  :root {
    --page-bg: #e9e9e9;
    --card-white: #fbfbfb;
    --navy: #0d3384;
    --navy-deep: #0a2a6e;
    --back-blue: #0b2f7a;
    --back-blue-dark: #07215a;
    --wordmark-on-blue: #1e5ed8;
    --text-grey: #55585e;
    --rule-grey: #8a8d92;
  }
  * { margin: 0; padding: 0; box-sizing: border-box; }
  html, body {
    width: 1200px; height: 801px; overflow: hidden;
    background: var(--page-bg);
    font-family: "Arimo", Arial, sans-serif;
  }
  .canvas {
    position: relative; width: 1200px; height: 801px;
    display: flex; align-items: center; justify-content: center; gap: 60px;
  }
  .card {
    position: relative; width: 520px; height: 298px;
    box-shadow: 0 6px 18px rgba(0,0,0,0.18);
    overflow: hidden;
  }
  /* Front */
  .card-front { background: var(--card-white); }
  .front-brand {
    position: absolute; top: 62px; left: 180px;
    display: flex; align-items: center; gap: 18px;
  }
  .brand-square { width: 40px; height: 40px; background: var(--navy); }
  .brand-name {
    font-weight: 700; font-size: 24px; letter-spacing: 9px;
    color: var(--navy); text-transform: uppercase;
  }
  .front-divider {
    position: absolute; top: 150px; left: 150px; right: 0;
    height: 1px; background: var(--rule-grey);
  }
  .contact-block { position: absolute; left: 40px; top: 168px; }
  .person-name { font-weight: 700; font-size: 19px; color: var(--navy); }
  .person-title { font-size: 15px; color: var(--text-grey); margin-top: 2px; }
  .contact-rule { width: 100px; height: 1px; background: var(--rule-grey); margin: 7px 0 6px; }
  .contact-list { list-style: none; }
  .contact-item {
    display: flex; align-items: center; gap: 8px;
    font-size: 13.5px; line-height: 17px; color: var(--text-grey);
  }
  .contact-icon { width: 12px; height: 12px; flex: none; }
  /* Back */
  .card-back {
    background: radial-gradient(ellipse at 45% 40%, var(--back-blue) 0%, var(--back-blue-dark) 100%);
    display: flex; align-items: center; justify-content: center;
  }
  .back-brand { display: flex; align-items: center; gap: 22px; }
  .back-brand .brand-square { width: 52px; height: 52px; background: var(--wordmark-on-blue); }
  .back-brand .brand-name { color: var(--wordmark-on-blue); font-size: 28px; letter-spacing: 11px; }
</style>
</head>
<body>
  <main class="canvas">
    <section class="card card-front" aria-label="Card front">
      <div class="front-brand">
        <span class="brand-square"></span>
        <span class="brand-name">Corvantis</span>
      </div>
      <div class="front-divider"></div>
      <div class="contact-block">
        <p class="person-name">Martin Keller</p>
        <p class="person-title">President &amp; CEO</p>
        <div class="contact-rule"></div>
        <ul class="contact-list">
          <li class="contact-item">
            <svg class="contact-icon" viewBox="0 0 12 12"><path d="M2.5 1 L4.5 1 L5 3.5 L3.8 4.3 C4.5 6 6 7.5 7.7 8.2 L8.5 7 L11 7.5 L11 9.5 C11 10.3 10.3 11 9.5 11 C5 11 1 7 1 2.5 C1 1.7 1.7 1 2.5 1 Z" fill="var(--navy)"/></svg>
            (415) 555-0182
          </li>
          <li class="contact-item">
            <svg class="contact-icon" viewBox="0 0 12 12"><rect x="3" y="0.8" width="6" height="10.4" rx="1" fill="none" stroke="var(--navy)" stroke-width="1.4"/></svg>
            (203) 555-0147
          </li>
          <li class="contact-item">
            <svg class="contact-icon" viewBox="0 0 12 12"><rect x="0.7" y="2.2" width="10.6" height="7.6" fill="var(--navy)"/><path d="M0.7 2.2 L6 6.5 L11.3 2.2 M0.7 9.8 L4.5 5.5 M11.3 9.8 L7.5 5.5" stroke="#fff" stroke-width="0.9" fill="none"/></svg>
            mkeller@corvantis.tech
          </li>
          <li class="contact-item">
            <svg class="contact-icon" viewBox="0 0 12 12"><circle cx="6" cy="6" r="5.3" fill="var(--navy)"/><path d="M0.7 6 H11.3 M6 0.7 C3.5 3.5 3.5 8.5 6 11.3 M6 0.7 C8.5 3.5 8.5 8.5 6 11.3" stroke="#fff" stroke-width="0.8" fill="none"/></svg>
            www.corvantis.tech
          </li>
        </ul>
      </div>
    </section>

    <section class="card card-back" aria-label="Card back">
      <div class="back-brand">
        <span class="brand-square"></span>
        <span class="brand-name">Corvantis</span>
      </div>
    </section>
  </main>
</body>
</html>
```